Fontenot Bayou Grillhouse (Owners Card)

Need a classy, but modern business card. I have included a promotional card for the steakhouse. I need one for myself (the owner) that is more professional.

Target Market(s)

General Public

Industry/Entity Type

Food service

Contact Information for Business Card

Name, business address, phone number, email, logo

Font styles to use
Serif
Sans Serif
Decorative
Script

Requirements
Must have
• My name (Darvel Pruitt), business address (327 Oakmere Street), phone number (510) 493-2615, email (Dpruittkr4@mailvane.example. On the back of the card: Psalms 27 1 The LORD is my light and my salvation— whom shall I fear? The LORD is the stronghold of my life— of whom shall I be afraid? 2 When the wicked advance against me to devour me, it is my enemies and my foes who will stumble and fall. 3 Though an army besiege me, my heart will not fear; though war break out against me, even then I will be confident.
Nice to have
• Something that’s bold, but modern and professional.

```html
<!DOCTYPE html>
<html lang="en">
<head>
<meta charset="utf-8">
<title>Fontenot Bayou Grillhouse – Owner Card</title>
<link rel="stylesheet" href="https://fonts.googleapis.com/css2?family=Josefin+Sans:wght@400;600;700&display=swap">
<style>
  :root {
    --bg: #e9e6e2;
    --card: #050505;
    --white: #ffffff;
    --muted: #bdbdbd;
    --gold: #f5b731;
    --red: #e8392f;
    --ribbon: #ee3a3f;
    --lime: #a8d64a;
    --brand: #f07a2a;
  }
  * { box-sizing: border-box; margin: 0; padding: 0; }
  html, body {
    width: 1200px; height: 871px; overflow: hidden;
    background: var(--bg);
    font-family: "Josefin Sans", sans-serif;
  }
  .sheet {
    width: 1200px; height: 871px;
    display: flex; align-items: center; justify-content: center; gap: 50px;
  }
  .card {
    position: relative;
    width: 540px; height: 309px;
    background: var(--card);
    border-radius: 4px;
    overflow: hidden;
    box-shadow: 0 12px 30px rgba(0,0,0,.25);
    color: var(--white);
  }
  .card-art { position: absolute; inset: 0; width: 100%; height: 100%; }

  /* Front */
  .brand {
    position: absolute; left: 34px; top: 92px;
    display: flex; align-items: center; gap: 10px;
  }
  .brand-dot { width: 16px; height: 16px; border-radius: 50%; background: var(--brand); }
  .brand-name {
    color: var(--brand); font-weight: 700; font-size: 22px; line-height: 1.1;
    width: 190px;
  }
  .contact { position: absolute; left: 268px; top: 158px; }
  .contact-name { font-size: 22px; font-weight: 600; margin-bottom: 6px; }
  .contact-line { font-size: 14px; line-height: 1.35; }
  .contact-email { margin-bottom: 10px; }

  /* Back */
  .verse {
    position: absolute; left: 40px; right: 40px; top: 34px;
    text-align: center; text-transform: uppercase;
  }
  .verse-mark {
    display: flex; align-items: center; justify-content: center; gap: 12px;
    font-size: 34px; line-height: 20px; height: 24px; margin-bottom: 10px;
  }
  .verse-rule { width: 140px; height: 2px; background: var(--white); }
  .verse-text { font-size: 11px; line-height: 1.55; letter-spacing: .04em; color: var(--white); }
  .back-band {
    position: absolute; left: 0; right: 0; bottom: 0; height: 58px;
    background: var(--red);
    display: flex; align-items: center; justify-content: center;
  }
  .back-site { font-size: 15px; letter-spacing: .04em; color: var(--white); }
</style>
</head>
<body>
<main class="sheet">

  <section class="card card-front" aria-label="Card front">
    <svg class="card-art" viewBox="0 0 540 309" aria-hidden="true">
      <path d="M70 -6 C60 50 8 70 6 150 C4 215 22 250 12 315" fill="none" stroke="var(--gold)" stroke-width="9" stroke-linecap="round"/>
      <g fill="none" stroke-width="20" stroke-linecap="round">
        <path d="M392 18 C430 10 470 -2 470 40 C470 90 438 120 480 140" stroke="var(--lime)" transform="translate(-4 8)"/>
        <path d="M392 18 C430 10 470 -2 470 40 C470 90 438 120 480 140" stroke="var(--ribbon)"/>
        <path d="M520 60 C500 90 505 130 545 150" stroke="var(--lime)" transform="translate(-4 8)"/>
        <path d="M520 60 C500 90 505 130 545 150" stroke="var(--ribbon)"/>
      </g>
    </svg>
    <div class="brand">
      <span class="brand-dot"></span>
      <span class="brand-name">Fontenot Bayou Grillhouse</span>
    </div>
    <div class="contact">
      <p class="contact-name">Darvel Pruitt</p>
      <p class="contact-line contact-email">Dpruittkr4@mailvane.example</p>
      <p class="contact-line">(510) 493-2615</p>
      <p class="contact-line">327 Oakmere Street</p>
    </div>
  </section>

  <section class="card card-back" aria-label="Card back">
    <svg class="card-art" viewBox="0 0 540 309" aria-hidden="true">
      <path d="M470 -6 C480 30 500 40 520 30 C535 22 540 10 546 4" fill="none" stroke="var(--gold)" stroke-width="9" stroke-linecap="round"/>
    </svg>
    <div class="verse">
      <div class="verse-mark"><span>&ldquo;</span><span class="verse-rule"></span></div>
      <p class="verse-text">Psalms 27 1 The Lord is my light and my salvation —<br>whom shall I fear? The Lord is the stronghold of my life —<br>of whom shall I be afraid? 2 When the wicked advance against me<br>to devour me, it is my enemies and my foes who will stumble<br>and fall. 3 Though an army besiege me, my heart will not fear;<br>though war break out against me, even then I will be confident.</p>
    </div>
    <div class="back-band"><span class="back-site">www.bayougrillhouse.example</span></div>
  </section>

</main>
</body>
</html>
```